Business Card Design Project

I need a business card designed from scratch. I have an existing logo that I can upload in Illustrator for modification or redesign.

The Company is called Rank Harbor http://rankharbor.com.au and we provide Search Engine Optimization services to Australian businesses. The current logo signifies an increase in visitors, profits etc...

There are no restrictions as to the redesign - colours, style etc are all open to change.

Cards will be full colour and one sided printed at http://www.printlorvex.com.au so check their requirements for file format and sizes etc.

I will expect all original files upon completion of project.

Target Market(s)

Any business with a web site looking to improve their search engine rankings

Industry/Entity Type

Business

Requirements
Must have
• I like modern, sleek designs. Clean, not fussy, uncluttered.

```html
<!DOCTYPE html>
<html lang="en">
<head>
<meta charset="utf-8">
<title>Rank Harbor Business Card</title>
<link rel="stylesheet" href="https://fonts.googleapis.com/css2?family=Arimo:wght@400;700&display=swap">
<style>
  :root {
    --page-bg: #ffffff;
    --card-bg: #ffffff;
    --brand-blue: #2a7dc1;
    --navy: #174a80;
    --sky: #2b8ad0;
    --gold: #f3c21a;
    --text-grey: #3a3a3a;
    --white: #ffffff;
  }
  * { margin: 0; padding: 0; box-sizing: border-box; }
  html, body {
    width: 1200px; height: 901px; overflow: hidden;
    background: var(--page-bg);
    font-family: "Arimo", Arial, sans-serif;
  }
  .business-card {
    position: absolute; left: 113px; top: 167px;
    width: 992px; height: 557px;
    background: var(--card-bg);
    overflow: hidden;
  }
  .brand {
    position: absolute; right: 52px; top: 103px;
    display: flex; align-items: center; gap: 18px;
  }
  .brand-dot {
    width: 34px; height: 34px; border-radius: 50%;
    background: var(--gold);
  }
  .brand-name {
    font-weight: 700; font-size: 58px; letter-spacing: -1px;
    color: var(--brand-blue); line-height: 1;
  }
  .contact {
    position: absolute; left: 72px; top: 246px;
    color: var(--text-grey); font-size: 25px; line-height: 33px;
  }
  .contact-line { display: flex; align-items: center; gap: 8px; }
  .contact-icon { width: 18px; height: 18px; fill: var(--brand-blue); flex: none; }
  .person {
    position: absolute; right: 52px; top: 259px; text-align: right;
  }
  .person-name {
    font-weight: 700; font-size: 31px; color: var(--brand-blue); line-height: 1.2;
  }
  .person-title {
    font-size: 24px; color: var(--text-grey); margin-top: 6px;
  }
  .footer-band {
    position: absolute; left: 0; right: 0; top: 470px; bottom: 0;
    border-top: 12px solid var(--gold);
    background: linear-gradient(90deg, var(--navy), var(--sky));
  }
  .web-address {
    position: absolute; right: 52px; top: 503px;
    font-size: 25px; color: var(--white);
  }
</style>
</head>
<body>
<div class="business-card">
  <div class="brand">
    <span class="brand-dot"></span>
    <span class="brand-name">Rank Harbor</span>
  </div>

  <div class="contact">
    <p>1870 Keller Road #204</p>
    <p>Tampa, FL 33602</p>
    <p class="contact-line">
      <svg class="contact-icon" viewBox="0 0 24 24"><path d="M6.6 10.8a15 15 0 0 0 6.6 6.6l2.2-2.2a1 1 0 0 1 1-.25 11.4 11.4 0 0 0 3.6.57 1 1 0 0 1 1 1V20a1 1 0 0 1-1 1A17 17 0 0 1 3 4a1 1 0 0 1 1-1h3.5a1 1 0 0 1 1 1 11.4 11.4 0 0 0 .57 3.6 1 1 0 0 1-.25 1z"/></svg>
      1300 584219
    </p>
    <p class="contact-line">
      <svg class="contact-icon" viewBox="0 0 24 24"><path d="M8 1h8a2 2 0 0 1 2 2v18a2 2 0 0 1-2 2H8a2 2 0 0 1-2-2V3a2 2 0 0 1 2-2zm0 3v14h8V4zm4 15.5a1 1 0 1 0 0 2 1 1 0 0 0 0-2z"/></svg>
      1300 584219
    </p>
    <p class="contact-line">
      <svg class="contact-icon" viewBox="0 0 24 24"><path d="M6 2h12v5H6zM3 8h18a2 2 0 0 1 2 2v7h-4v5H5v-5H1v-7a2 2 0 0 1 2-2zm4 8v4h10v-4z"/></svg>
      1300 584219
    </p>
    <p class="contact-line">
      <svg class="contact-icon" viewBox="0 0 24 24"><path d="M2 5h20v2l-10 6L2 7zm0 4.3l10 6 10-6V19H2z"/></svg>
      enquiry@rankharbor.com.au
    </p>
  </div>

  <div class="person">
    <p class="person-name">Daniel Whitford</p>
    <p class="person-title">Founder &amp; CEO</p>
  </div>

  <div class="footer-band" role="img" aria-label="Decorative yellow and blue wave artwork area"></div>
  <p class="web-address">www.rankharbor.com.au</p>
</div>
</body>
</html>
```